Qorby Labs

I am a CBD Manufacturer I would have a site more laid out in a lab format
current site is qorbylabs.example what Id like is a site like tarnwellabs.example

Target Market(s)

Any one needing cbd oil and finished goods

Coding

Coded - Design and coding required

Number of Pages Required

1 page

```html
<!DOCTYPE html>
<html lang="en">
<head>
<meta charset="utf-8">
<title>Qorby Labs</title>
<link href="https://fonts.googleapis.com/css2?family=Montserrat:wght@400;500;600;700&family=Open+Sans:wght@400;600&display=swap" rel="stylesheet">
<style>
:root{
  --teal:#1f7585;
  --teal-dark:#1a6676;
  --ink:#222;
  --muted:#444;
  --header:#dcdcdc;
  --panel:#f0f0f0;
  --footer:#ededed;
  --white:#fff;
  --rule:#b9b9b9;
}
*{margin:0;padding:0;box-sizing:border-box}
html,body{width:1200px;height:1200px;overflow:hidden;background:var(--white)}
body{position:relative;font-family:"Open Sans",sans-serif;color:var(--ink)}
.page{position:absolute;left:275px;top:0;width:650px;height:1200px}
.abs{position:absolute}
.site-header{left:0;top:0;width:650px;height:36px;background:var(--header);border-bottom:1px solid #b8c7ca}
.brand{display:flex;align-items:center;gap:5px;font-family:"Montserrat",sans-serif;font-weight:700;color:var(--teal);font-size:13px;letter-spacing:.3px}
.brand-mark{width:10px;height:10px;background:var(--teal)}
.site-header .brand{position:absolute;left:61px;top:11px}
.nav{position:absolute;left:382px;top:13px;display:flex;gap:12px;font-family:"Montserrat",sans-serif;font-size:8.5px;font-weight:500;color:#111}
.cart{position:absolute;left:558px;top:10px}
.mission{left:0;top:36px;width:650px;height:154px;background:var(--teal);color:var(--white)}
.mission h2{position:absolute;left:0;width:650px;top:33px;text-align:center;font-family:"Montserrat",sans-serif;font-size:12.5px;font-weight:600;letter-spacing:1px}
.mission p{position:absolute;left:157px;top:56px;width:340px;font-size:8.6px;line-height:11.4px;letter-spacing:.2px}
.photo{background:linear-gradient(135deg,#eef1f5,#c9d2dc)}
.photo-lab{left:0;top:190px;width:328px;height:226px;background:linear-gradient(120deg,#f3f5f8 0%,#dfe5ec 55%,#aeb9c4 100%)}
.photo-drops{left:327px;top:416px;width:323px;height:215px;background:linear-gradient(110deg,#e9ebea 0%,#c7b9a8 45%,#7d8c90 70%,#3e8fb0 100%)}
.section-title{font-family:"Montserrat",sans-serif;font-weight:600;color:var(--teal);font-size:12px;letter-spacing:.2px}
.copy{font-size:8.4px;line-height:11.4px;letter-spacing:.45px;color:var(--muted)}
.copy a{color:var(--teal);text-decoration:none}
.team{left:0;top:631px;width:650px;height:256px;background:var(--panel)}
.team h2{position:absolute;left:0;width:650px;top:39px;text-align:center}
.card{position:absolute;top:75px;width:129px;height:139px;background:var(--white)}
.card.raised{box-shadow:0 5px 10px rgba(0,0,0,.15)}
.card .portrait{width:129px;height:103px}
.card h3{font-family:"Montserrat",sans-serif;font-size:7px;font-weight:700;text-align:center;margin-top:9px}
.card p{font-size:5px;font-style:italic;text-align:center;color:#777;margin-top:2px}
.newsletter h2{position:absolute;left:0;width:650px;top:926px;text-align:center;font-size:12.5px}
.field-label{font-family:"Montserrat",sans-serif;font-size:6.5px;font-weight:500}
.field{border:1px solid #cfcfcf;border-radius:4px;background:var(--white);height:21px}
.submit{left:435px;top:968px;width:119px;height:21px;border-radius:11px;background:var(--teal);color:var(--white);font-family:"Montserrat",sans-serif;font-size:6.5px;font-weight:700;letter-spacing:.6px;display:flex;align-items:center;justify-content:center}
.site-footer{left:0;top:1033px;width:650px;height:167px;background:var(--footer);font-family:"Montserrat",sans-serif}
.site-footer .brand{position:absolute;left:61px;top:24px}
.contact{position:absolute;left:61px;top:57px;font-size:6.8px;line-height:13px;color:#333}
.contact a{color:var(--teal);text-decoration:none}
.contact .hours{line-height:8px;margin-top:1px}
.foot-head{position:absolute;top:45px;font-size:8px;font-weight:600;color:var(--teal);letter-spacing:.3px}
.disclaimer{position:absolute;left:184px;top:60px;width:170px;font-size:6.6px;line-height:10px;color:#333}
.links{position:absolute;top:57px;font-size:6.6px;line-height:12.6px;color:#333;list-style:none}
.foot-rule{position:absolute;left:62px;top:131px;width:528px;height:1px;background:var(--rule)}
.copyright{position:absolute;left:0;width:650px;top:146px;text-align:center;font-size:5.8px;color:var(--teal)}
</style>
</head>
<body>
<div class="page">
  <header class="abs site-header">
    <div class="brand"><span class="brand-mark"></span>Qorby Labs</div>
    <nav class="nav"><span>HOME</span><span>ABOUT US</span><span>SHOP</span><span>CONTACT</span></nav>
    <svg class="cart" width="18" height="16" viewBox="0 0 18 16" aria-label="Cart">
      <path d="M1 3h3l2 7h8l2-5H5" fill="none" stroke="#333" stroke-width="1"/>
      <circle cx="7" cy="13" r="1.2" fill="#333"/><circle cx="13" cy="13" r="1.2" fill="#333"/>
      <circle cx="15" cy="3" r="2.6" fill="var(--teal)"/>
    </svg>
  </header>

  <section class="abs mission">
    <h2>Mission</h2>
    <p>Our mission is to make a positive impact on humanity and the world, one day at a time. We pride ourselves on delivering our customers the highest quality full spectrum CBD infused products. Our products are made using the finest-quality, natural ingredients, and contains only hemp sourced domestically in the U.S.</p>
  </section>

  <div class="abs photo-lab" role="img" aria-label="Lab technician in white coat and hairnet operating production equipment"></div>
  <h2 class="abs section-title" style="left:369px;top:266px">About Us</h2>
  <p class="abs copy" style="left:369px;top:286px;width:260px">Qorby Labs prides itself on delivering our customers the highest quality full spectrum CBD infused products. Our products are made using the finest-quality, natural ingredients, and contain only 100% hemp sourced in the U.S</p>

  <h2 class="abs section-title" style="left:59px;top:466px">Customer Satisfaction</h2>
  <p class="abs copy" style="left:55px;top:487px;width:260px">Qorby Labs strives to make every customer satisfied with their purchase. Every product goes through 100% Quality Control inspection, are securely sealed and packed to ensure your order is delivered to you safely. In the event that your package does not arrive as expected, or you are not completely satisfied, please contact us at <a>info@qorbylabs.example</a> and we will do our best to meet your needs.</p>
  <div class="abs photo-drops" role="img" aria-label="Hand adding drops of CBD oil from a dropper bottle into a mug"></div>

  <section class="abs team">
    <h2 class="section-title">Our Team</h2>
    <div class="card" style="left:46px"><div class="portrait" role="img" aria-label="Team member portrait" style="background:linear-gradient(135deg,#e8e8e8,#777)"></div><h3>Name 1</h3><p>Title</p></div>
    <div class="card" style="left:189px"><div class="portrait" role="img" aria-label="Team member portrait" style="background:linear-gradient(135deg,#b7a690,#5a4a3c)"></div><h3>Name 2</h3><p>Title</p></div>
    <div class="card" style="left:332px"><div class="portrait" role="img" aria-label="Team member portrait" style="background:linear-gradient(135deg,#f2f2f2,#9fa8b4)"></div><h3>Name 3</h3><p>Title</p></div>
    <div class="card raised" style="left:476px"><div class="portrait" role="img" aria-label="Team member portrait" style="background:linear-gradient(135deg,#3f6fa0,#1e3452)"></div><h3>Name 4</h3><p>Title</p></div>
  </section>

  <section class="newsletter">
    <h2 class="section-title">Subscribe to Our Newsletter</h2>
    <span class="abs field-label" style="left:106px;top:958px">Name</span>
    <div class="abs field" style="left:106px;top:969px;width:167px"></div>
    <span class="abs field-label" style="left:286px;top:957px">Email</span>
    <div class="abs field" style="left:286px;top:968px;width:137px"></div>
    <div class="abs submit">SUBMIT</div>
  </section>

  <footer class="abs site-footer">
    <div class="brand"><span class="brand-mark"></span>Qorby Labs</div>
    <div class="contact">
      48 Orchard Row<br>Fenmore, CA 90017<br>1-800-555-0199<br><a>info@qorbylabs.example</a>
      <div class="hours">Monday - Friday<br>8:00 AM - 5:00 PM CT</div>
    </div>
    <h3 class="foot-head" style="left:184px">DISCLAIMER</h3>
    <p class="disclaimer">The statements regarding these products have not been evaluated by the Food and Drug Administration. These products are not intended to diagnose, treat, cure or prevent any disease. Results from products may vary.</p>
    <h3 class="foot-head" style="left:397px">QUICK LINKS</h3>
    <ul class="links" style="left:397px"><li>Mission</li><li>Customer Satisfaction</li><li>Shipping &amp; Return Policy</li><li>Privacy Policy</li><li>Terms of Service</li></ul>
    <h3 class="foot-head" style="left:535px">FOLLOW US</h3>
    <ul class="links" style="left:535px"><li>Facefeed</li><li>Chirper</li><li>Snapgram</li></ul>
    <div class="foot-rule"></div>
    <p class="copyright">© 2020 Qorby Labs. All Rights Reserved.</p>
  </footer>
</div>
</body>
</html>
```